Label design, for stand up guayusa tea pouch.

I need a high quality, clean, modern sticker label design. Its going on a stand up tea pouch. The front of the pouch is transparent, with a foil back. The foil back is visible from front view.The product is a dark green herb. its in the form of loose leaf tea. Guayusa provides clean energy. Its main point is that its an alternative to coffee with similar caffeine levels, but it doesn't give the same jittery feeling as coffee because of a component called theobromine.

Target Market(s)

Men and women 18-65

Font styles to use
Sans Serif
Decorative

Colors

Designer to choose colors to be used in the design.

Requirements
Must have
• -Logo provided: icon
• The logo icon colors can be changed to have some green if it will work better
• -Brand: Lanternpeak guayusa
• -A background that goes well with the packaging (transparent/foil) picture provided
Should not have
• Blank background
• Overly loud background

```html
<!DOCTYPE html>
<html lang="en">
<head>
<meta charset="utf-8">
<title>Lanternpeak tea – Guayusa Blend Tea label</title>
<link rel="stylesheet" href="https://fonts.googleapis.com/css2?family=Barlow+Semi+Condensed:wght@400;500;600&family=Barlow:wght@600&family=Tenor+Sans&display=swap">
<style>
  :root {
    --canvas-bg: #ffffff;
    --brand-ink: #2f3133;
    --brand-mark: #e59a22;
    --title-green: #1e6b37;
    --tag-green: #2b7a3c;
    --rule-green: #2e6e3e;
    --badge-ring: #f0b43a;
    --badge-fill: #e9a12a;
    --icon-ink: #ffffff;
    --body-ink: #2b2b2b;
  }
  * { margin: 0; padding: 0; box-sizing: border-box; }
  html, body {
    width: 1200px;
    height: 1200px;
    overflow: hidden;
    background: var(--canvas-bg);
  }
  .label {
    position: relative;
    width: 1200px;
    height: 1200px;
    background: var(--canvas-bg);
  }
  .label-column {
    position: absolute;
    top: 0;
    left: 0;
    width: 1132px;
    height: 1200px;
    text-align: center;
  }
  .brand-mark {
    position: absolute;
    top: 318px;
    left: 496px;
    width: 140px;
    height: 140px;
    border-radius: 50%;
    background: var(--brand-mark);
  }
  .brand-name {
    position: absolute;
    top: 518px;
    left: 0;
    width: 100%;
    font-family: "Barlow", sans-serif;
    font-weight: 600;
    font-size: 35px;
    color: var(--brand-ink);
  }
  .product-title {
    position: absolute;
    top: 600px;
    left: 0;
    width: 100%;
    font-family: "Tenor Sans", sans-serif;
    font-weight: 400;
    font-size: 63px;
    letter-spacing: 2px;
    color: var(--title-green);
    line-height: 1;
    -webkit-text-stroke: 1.2px var(--title-green);
  }
  .product-subtitle {
    position: absolute;
    top: 680px;
    left: 0;
    width: 100%;
    font-family: "Barlow Semi Condensed", sans-serif;
    font-weight: 400;
    font-size: 28px;
    letter-spacing: 1.6px;
    color: var(--title-green);
  }
  .title-rule {
    position: absolute;
    top: 730px;
    left: 455px;
    width: 226px;
    height: 2px;
    background: var(--rule-green);
  }
  .tagline {
    position: absolute;
    top: 758px;
    left: 0;
    width: 100%;
    font-family: "Barlow Semi Condensed", sans-serif;
    font-weight: 600;
    font-size: 18px;
    letter-spacing: 1px;
    color: var(--tag-green);
  }
  .benefit {
    position: absolute;
    top: 815px;
    width: 160px;
    margin-left: -80px;
    font-family: "Barlow Semi Condensed", sans-serif;
    font-weight: 500;
    font-size: 18px;
    line-height: 1.3;
    color: var(--body-ink);
  }
  .benefit--coffee { left: 419px; }
  .benefit--theobromine { left: 565px; }
  .benefit--leaf { left: 714px; }
  .benefit-badge {
    display: block;
    width: 100px;
    height: 100px;
    margin: 0 auto 14px;
  }
  .benefit--theobromine .benefit-text { padding-top: 12px; }
  .badge-icon {
    fill: none;
    stroke: var(--icon-ink);
    stroke-width: 2.2;
    stroke-linecap: round;
    stroke-linejoin: round;
  }
  .net-weight {
    position: absolute;
    top: 1022px;
    left: 0;
    width: 100%;
    font-family: "Barlow Semi Condensed", sans-serif;
    font-weight: 500;
    font-size: 18px;
    color: var(--body-ink);
  }
</style>
</head>
<body>
<main class="label">
  <div class="label-column">
    <div class="brand-mark" aria-hidden="true"></div>
    <div class="brand-name">Lanternpeak tea</div>

    <h1 class="product-title">GUAYUSA</h1>
    <div class="product-subtitle">BLEND TEA</div>
    <div class="title-rule"></div>

    <p class="tagline">PROVIDES CLEAN ENERGY TO THE BODY</p>

    <div class="benefit benefit--coffee">
      <svg class="benefit-badge" viewBox="0 0 100 100" role="img" aria-label="Steaming cup icon">
        <circle cx="50" cy="50" r="48" fill="none" stroke="var(--badge-ring)" stroke-width="2.5"/>
        <circle cx="50" cy="50" r="42" fill="var(--badge-fill)"/>
        <g class="badge-icon">
          <path d="M30 52 h34 v6 a12 12 0 0 1 -12 12 h-10 a12 12 0 0 1 -12 -12 z"/>
          <path d="M64 55 h4 a5 5 0 0 1 0 10 h-5"/>
          <path d="M28 74 h40"/>
          <path d="M40 46 c-4 -4 4 -7 0 -12 c-3 -4 2 -6 1 -9"/>
          <path d="M48 46 c-4 -4 4 -7 0 -12 c-3 -4 2 -6 1 -9"/>
          <path d="M56 46 c-4 -4 4 -7 0 -12 c-3 -4 2 -6 1 -9"/>
        </g>
      </svg>
      <div class="benefit-text">Coffee<br>Alternative</div>
    </div>

    <div class="benefit benefit--theobromine">
      <svg class="benefit-badge" viewBox="0 0 100 100" role="img" aria-label="Cacao pod icon">
        <circle cx="50" cy="50" r="48" fill="none" stroke="var(--badge-ring)" stroke-width="2.5"/>
        <circle cx="50" cy="50" r="42" fill="var(--badge-fill)"/>
        <g class="badge-icon">
          <path d="M50 30 c-10 8 -12 22 -10 32 c2 8 6 12 10 14 c4 -2 8 -6 10 -14 c2 -10 0 -24 -10 -32 z"/>
          <path d="M50 31 v44"/>
          <path d="M45 36 c-3 10 -3 24 2 36"/>
          <path d="M55 36 c3 10 3 24 -2 36"/>
          <path d="M50 30 c2 -4 6 -6 10 -6 c-2 4 -6 6 -10 6"/>
        </g>
      </svg>
      <div class="benefit-text">Theobromine</div>
    </div>

    <div class="benefit benefit--leaf">
      <svg class="benefit-badge" viewBox="0 0 100 100" role="img" aria-label="Two leaves icon">
        <circle cx="50" cy="50" r="48" fill="none" stroke="var(--badge-ring)" stroke-width="2.5"/>
        <circle cx="50" cy="50" r="42" fill="var(--badge-fill)"/>
        <g class="badge-icon">
          <path d="M48 70 c-14 0 -22 -12 -20 -32 c16 2 24 14 20 32 z"/>
          <path d="M48 70 l-16 -28"/>
          <path d="M52 70 c14 0 22 -12 20 -32 c-16 2 -24 14 -20 32 z"/>
          <path d="M52 70 l16 -28"/>
          <path d="M50 70 v6"/>
        </g>
      </svg>
      <div class="benefit-text">100%<br>Guayusa</div>
    </div>

    <p class="net-weight">NET WT. 113 oz (32 g)</p>
  </div>
</main>
</body>
</html>
```